Seeking funky, innovative business cards

I am looking to refresh our current business cards to something more engaging, visual and impactful. We are a management consultancy firm, see website (www.larkspur-advisory.com.au). I've included our colour scheme, sample of the slides we use and our old business cards. We would like our cards to have icons. The card should display:- Name- Title- Mobile number- Address- Email address- Website - Company logo- Our purpose statement "We shape workplaces people love to work in"

Contact Information for Business Card

Tavish Brellan
Consultant
0491 672 348
Level 5, 218 Warrick Lane, Melbourne 3000
tavish@larkspur-advisory.com.au
www.larkspur-advisory.com.au

Purpose statement "We shape workplaces people love to work in"
LOGO available in google images

Font styles to use
Other font styles liked:
• Open Sans Light, Bebas Neue (open to other cool foints)

Colors
ffc214
5c5c5c
f5f5f5
fefefe

Requirements
Must have
• - Name
• - Title
• - Mobile number
• - Address
• - Email address
• - Website
• - Company logo
• - Our purpose statement "We shape workplaces people love to work in"
Nice to have
• - Icons
• - Colour (see our colour scheme"

```html
<!DOCTYPE html>
<html lang="en">
<head>
<meta charset="utf-8">
<title>Larkspur Advisory – Business Cards</title>
<link href="https://fonts.googleapis.com/css2?family=Bebas+Neue&family=Open+Sans:wght@300;400;600&display=swap" rel="stylesheet">
<style>
  :root {
    --brand-yellow: #ffc214;
    --brand-orange: #f5a32c;
    --ink-grey: #5c5c5c;
    --ink-dark: #3f3f3f;
    --card-white: #fefefe;
    --backdrop: #e9e9e9;
  }
  * { margin: 0; padding: 0; box-sizing: border-box; }
  html, body {
    width: 1200px; height: 900px; overflow: hidden;
    background: var(--backdrop);
    font-family: "Open Sans", Arial, sans-serif;
    color: var(--ink-grey);
  }
  .sheet {
    width: 1200px; height: 900px;
    display: flex; flex-direction: column; align-items: center; justify-content: center;
    gap: 44px;
  }
  .card {
    position: relative;
    width: 700px; height: 400px;
    background: var(--card-white);
    border-radius: 28px;
    overflow: hidden;
    box-shadow: 0 2px 0 #d4d4d4, 0 10px 24px rgba(0,0,0,0.12);
  }

  /* Front */
  .card-front .wordmark {
    position: absolute; left: 0; right: 0; top: 120px;
    display: flex; align-items: center; justify-content: center; gap: 18px;
  }
  .wordmark-dot {
    width: 22px; height: 22px; border-radius: 50%;
    background: var(--brand-yellow);
    flex: none;
  }
  .wordmark-name {
    font-weight: 300; font-size: 64px; letter-spacing: 1px;
    color: var(--ink-dark); line-height: 1; white-space: nowrap;
  }
  .purpose-band {
    position: absolute; left: 0; right: 0; bottom: 0; height: 72px;
    background: linear-gradient(90deg, var(--brand-yellow), var(--brand-orange));
    display: flex; align-items: center; padding-left: 44px;
  }
  .purpose-text {
    font-weight: 600; font-style: italic; font-size: 21px;
    color: var(--ink-dark);
  }

  /* Back */
  .card-back .identity { position: absolute; left: 46px; top: 38px; }
  .person-name {
    font-family: "Bebas Neue", Impact, sans-serif;
    font-weight: 400;
    font-size: 40px; line-height: 1; letter-spacing: 0.5px; color: var(--ink-dark);
  }
  .person-title { font-size: 18px; margin-top: 2px; }
  .address {
    position: absolute; left: 46px; top: 140px;
    font-size: 16px; line-height: 1.35;
  }
  .contact-list {
    position: absolute; left: 46px; top: 220px;
    list-style: none; display: flex; flex-direction: column; gap: 12px;
  }
  .contact-item { display: flex; align-items: center; gap: 14px; font-size: 16px; }
  .contact-icon {
    width: 30px; height: 30px; border-radius: 50%;
    background: var(--brand-yellow);
    display: flex; align-items: center; justify-content: center; flex: none;
  }
  .card-back .wordmark {
    position: absolute; right: 46px; top: 150px;
    display: flex; align-items: center; gap: 12px;
  }
  .card-back .wordmark-name { font-size: 38px; }
  .card-back .wordmark-dot { width: 16px; height: 16px; }
</style>
</head>
<body>
<main class="sheet">

  <section class="card card-front" aria-label="Business card front">
    <div class="wordmark">
      <span class="wordmark-dot"></span>
      <span class="wordmark-name">Larkspur Advisory</span>
    </div>
    <div class="purpose-band">
      <p class="purpose-text">We shape workplaces people love to work in</p>
    </div>
  </section>

  <section class="card card-back" aria-label="Business card back">
    <div class="identity">
      <h1 class="person-name">Tavish Brellan</h1>
      <p class="person-title">Consultant</p>
    </div>
    <p class="address">Level 5, 218 Warrick Lane<br>Melbourne 3000</p>
    <ul class="contact-list">
      <li class="contact-item">
        <span class="contact-icon">
          <svg width="14" height="16" viewBox="0 0 14 16" aria-hidden="true"><rect x="3" y="1" width="8" height="14" rx="1.5" fill="none" stroke="#3f3f3f" stroke-width="1.6"/><circle cx="7" cy="12.5" r="0.9" fill="#3f3f3f"/></svg>
        </span>
        0491 672 348
      </li>
      <li class="contact-item">
        <span class="contact-icon">
          <svg width="16" height="12" viewBox="0 0 16 12" aria-hidden="true"><rect x="1" y="1" width="14" height="10" rx="1" fill="#3f3f3f"/><path d="M1.5 1.5 L8 7 L14.5 1.5" fill="none" stroke="#ffc214" stroke-width="1.3"/></svg>
        </span>
        tavish@larkspur-advisory.com.au
      </li>
      <li class="contact-item">
        <span class="contact-icon">
          <svg width="16" height="16" viewBox="0 0 16 16" aria-hidden="true"><g fill="none" stroke="#3f3f3f" stroke-width="1.3"><circle cx="8" cy="8" r="6.5"/><ellipse cx="8" cy="8" rx="2.8" ry="6.5"/><path d="M1.5 8 H14.5 M2.5 4.5 H13.5 M2.5 11.5 H13.5"/></g></svg>
        </span>
        www.larkspur-advisory.com.au
      </li>
    </ul>
    <div class="wordmark">
      <span class="wordmark-dot"></span>
      <span class="wordmark-name">Larkspur Advisory</span>
    </div>
  </section>

</main>
</body>
</html>
```